Use responsive design to make this page look and behave awesome in any size

YOU CAN SUBMIT PSD, HOWEVER, THE WINNER MUST SUBMIT PROVIDE A SINGLE CODED PAGE PER THE LINK AND INSTRUCTIONS AT THE BOTTOM OF THIS BRIEF. While developing an internal website, we realized we are not super great at making things look awesome and responsive for phone/tablet/desktop. Thats where you come in. We want you to take this code, Fork it, and then make it look awesome and work great on any size device.

Task at hand:

This page is a simple dashboard showing how a number of stores stack up against each other and against a corporate goal.

Top: Goal title, and where the logged in person's store stands in the ranking.
Green means you are in compliance
Red means you are not in compliance

Middle: Description of goal. Words to describe what the corporate goal is, and a target number.

Bottom: Here we just want to show the top 10 and bottom 5 out of 100+ stores. if your in the top ten, you are highlighted. If your in the bottom 5, you will be highlighted there too. If you are in the middle, we would put the your store info between the top and bottom... indicating your in the middle.
Green means you they are in compliance
Red means they are not in compliance

Your Mission is not only to make this look fantastic and responsive, but to have usable code in there.

You don't need to do any logic. All we care about is look and feel and responsive behavior on different size browsers.

The winner obviously gets the prize, and hopefully can become a solid resource to do more of this type of thing for us in the future.

Instructions:
Go to this link: https://codequill.example/edit/tvx-leaderpanel-widget
Click on the blue Fork button. This will give you a new URL that you can paste back into the contest to review results for us to see your work.
Uploading pictures is not necessary as the responsive code is what is important here.

Good luck!

Number of Pages Required

1 page

Requirements
Must have
• The page must be responsive and look very professional AND game like.
Should not have
• plugins. just native code

```html
<!DOCTYPE html>
<html lang="en">
<head>
<meta charset="UTF-8">
<title>Lead Measures</title>
<link href="https://fonts.googleapis.com/css2?family=Raleway:wght@400;500;600;700&display=swap" rel="stylesheet">
<style>
  :root {
    --band-start: #5a6ee2;
    --band-end: #8a5be3;
    --page-bg: #ececec;
    --card-bg: #ffffff;
    --accent-green: #2ecf8b;
    --badge-green: #23b25c;
    --text-green: #22b15a;
    --text-red: #e8485a;
    --alert-red: #dc3545;
    --ink: #333a44;
    --line: #dedede;
    --bubble: rgba(255, 255, 255, 0.16);
  }
  * { box-sizing: border-box; margin: 0; padding: 0; }
  html, body { width: 1200px; height: 675px; overflow: hidden; }
  body {
    font-family: "Raleway", sans-serif;
    background: var(--page-bg);
    color: var(--ink);
    position: relative;
  }
  .hero-band {
    position: absolute; left: 0; top: 0; width: 1200px; height: 270px;
    background: linear-gradient(100deg, var(--band-start), var(--band-end));
  }
  .hero-bubbles { position: absolute; inset: 0; }
  .page-title {
    position: absolute; top: 58px; left: 0; width: 100%;
    text-align: center; color: #fff; font-weight: 400;
    font-size: 35px; letter-spacing: 0.5px;
  }
  .measure-grid {
    position: absolute; top: 138px; left: 25px;
    display: flex; gap: 24px;
  }
  .measure-card {
    width: 270px; height: 560px; background: var(--card-bg);
  }
  .card-head {
    height: 45px; background: var(--accent-green); color: #fff;
    display: flex; align-items: center; justify-content: center; gap: 16px;
    font-weight: 700; font-size: 17px;
  }
  .card-head .score { font-size: 16px; }
  .goal {
    display: flex; justify-content: space-between; align-items: flex-start;
    padding: 16px 16px 12px 16px;
  }
  .goal-text { font-size: 12.5px; line-height: 1.25; width: 150px; color: #3d444d; }
  .goal-target {
    background: var(--badge-green); color: #fff; font-weight: 700;
    font-size: 11px; padding: 6px 7px; border-radius: 2px; margin-right: 22px;
  }
  .rank-list { list-style: none; margin: 0 16px; }
  .rank-row {
    height: 40.5px; border: 1px solid var(--line); border-bottom: none;
    display: flex; align-items: center; padding: 0 16px; font-size: 13px;
  }
  .rank-row:last-child { border-bottom: 1px solid var(--line); }
  .rank-pos { color: var(--ink); width: 14px; font-size: 12px; font-weight: 600; }
  .store-name { flex: 1; margin-left: 0; }
  .is-red .store-name, .is-red .metric { color: var(--text-red); }
  .is-green .store-name, .is-green .metric { color: var(--text-green); }
  .metric { font-size: 12.5px; }
  .rank-row.is-you {
    background: var(--alert-red); border-color: var(--alert-red); color: #fff;
  }
  .is-you .store-name, .is-you .metric, .is-you .rank-pos { color: #fff; }
</style>
</head>
<body>
  <div class="hero-band">
    <svg class="hero-bubbles" width="1200" height="270" aria-hidden="true">
      <circle cx="125" cy="65" r="40" fill="var(--bubble)"/>
      <circle cx="301" cy="24" r="61" fill="var(--bubble)"/>
      <circle cx="800" cy="65" r="40" fill="var(--bubble)"/>
      <circle cx="1117" cy="37" r="61" fill="var(--bubble)"/>
    </svg>
    <h1 class="page-title">LEAD MEASURES</h1>
  </div>

  <main class="measure-grid">
    <section class="measure-card">
      <header class="card-head"><span>TEAM</span><span class="score">92.1%</span></header>
      <div class="goal"><p class="goal-text">Use Slow Stock wherever possible</p><span class="goal-target">80%</span></div>
      <ol class="rank-list">
        <li class="rank-row is-red"><span class="rank-pos">1</span><span class="store-name">(1) yjcQbtCyQu</span><span class="metric">1%</span></li>
        <li class="rank-row is-red"><span class="rank-pos">2</span><span class="store-name">(1) crsmicfXwS</span><span class="metric">1%</span></li>
        <li class="rank-row is-red"><span class="rank-pos">3</span><span class="store-name">(2) wnLJojLRSf</span><span class="metric">2%</span></li>
        <li class="rank-row is-red"><span class="rank-pos">4</span><span class="store-name">(2) swEbjeRrpi</span><span class="metric">2%</span></li>
        <li class="rank-row is-red"><span class="rank-pos">5</span><span class="store-name">(4) oUauMPncOA</span><span class="metric">4%</span></li>
        <li class="rank-row is-red"><span class="rank-pos">6</span><span class="store-name">(5) vYuFdHZExR</span><span class="metric">5%</span></li>
        <li class="rank-row is-red"><span class="rank-pos">7</span><span class="store-name">(5) jvBnNaGkeE</span><span class="metric">5%</span></li>
        <li class="rank-row is-red"><span class="rank-pos">8</span><span class="store-name">(6) CuWlIvexCs</span><span class="metric">6%</span></li>
        <li class="rank-row is-red"><span class="rank-pos">9</span><span class="store-name">(7) XQFCUbSoko</span><span class="metric">7%</span></li>
        <li class="rank-row is-red"><span class="rank-pos">10</span><span class="store-name">&nbsp;(7) GucpFDVVJP</span><span class="metric">7%</span></li>
      </ol>
    </section>

    <section class="measure-card">
      <header class="card-head"><span>SLOW</span><span class="score">0%</span></header>
      <div class="goal"><p class="goal-text">Less than 0% of inventory slower than 100 days</p><span class="goal-target">&lt; 1%</span></div>
      <ol class="rank-list">
        <li class="rank-row is-green"><span class="rank-pos">1</span><span class="store-name">(89) NZBGVulmnc</span><span class="metric">0%</span></li>
        <li class="rank-row is-green"><span class="rank-pos">2</span><span class="store-name">(80) GaccDehKUO</span><span class="metric">0%</span></li>
        <li class="rank-row is-green"><span class="rank-pos">3</span><span class="store-name">(55) aPfpNcqcDh</span><span class="metric">0%</span></li>
        <li class="rank-row is-green"><span class="rank-pos">4</span><span class="store-name">(97) YqyVfKlTIL</span><span class="metric">0%</span></li>
        <li class="rank-row is-green"><span class="rank-pos">5</span><span class="store-name">(67) PvQdqyeaHr</span><span class="metric">0%</span></li>
        <li class="rank-row is-you"><span class="rank-pos">6</span><span class="store-name">(00) Your Store</span><span class="metric">2%</span></li>
        <li class="rank-row is-red"><span class="rank-pos">7</span><span class="store-name">(40) jyMfVYlVbl</span><span class="metric">2%</span></li>
        <li class="rank-row is-red"><span class="rank-pos">8</span><span class="store-name">(11) QSESmpDJqw</span><span class="metric">2%</span></li>
        <li class="rank-row is-red"><span class="rank-pos">9</span><span class="store-name">(71) nIlaXFpJWv</span><span class="metric">2%</span></li>
        <li class="rank-row is-red"><span class="rank-pos">10</span><span class="store-name">&nbsp;(51) ENrkkveKpb</span><span class="metric">2%</span></li>
      </ol>
    </section>

    <section class="measure-card">
      <header class="card-head"><span>TURNS</span><span class="score">2.2</span></header>
      <div class="goal"><p class="goal-text">Turn inventory 6 or more times a year</p><span class="goal-target">&gt; 6</span></div>
      <ol class="rank-list">
        <li class="rank-row is-red"><span class="rank-pos">1</span><span class="store-name">(8) VZaEOSVkef</span><span class="metric">0.2</span></li>
        <li class="rank-row is-red"><span class="rank-pos">2</span><span class="store-name">(3) PcVKNpUNmj</span><span class="metric">0.2</span></li>
        <li class="rank-row is-red"><span class="rank-pos">3</span><span class="store-name">(4) RllyRZsTIn</span><span class="metric">0.4</span></li>
        <li class="rank-row is-red"><span class="rank-pos">4</span><span class="store-name">(9) epiNQFtERO</span><span class="metric">0.6</span></li>
        <li class="rank-row is-red"><span class="rank-pos">5</span><span class="store-name">(3) FbFOzkjSpF</span><span class="metric">0.7</span></li>
        <li class="rank-row is-red"><span class="rank-pos">6</span><span class="store-name">(7) RdzzkcVqtC</span><span class="metric">0.8</span></li>
        <li class="rank-row is-red"><span class="rank-pos">7</span><span class="store-name">(1) DiilXiGkTx</span><span class="metric">0.8</span></li>
        <li class="rank-row is-red"><span class="rank-pos">8</span><span class="store-name">(1) jxWbwORyVa</span><span class="metric">0.8</span></li>
        <li class="rank-row is-red"><span class="rank-pos">9</span><span class="store-name">(4) UyzYfIMzU</span><span class="metric">0.8</span></li>
        <li class="rank-row is-red"><span class="rank-pos">10</span><span class="store-name">&nbsp;(4) KVlgJQBgAc</span><span class="metric">1</span></li>
      </ol>
    </section>

    <section class="measure-card">
      <header class="card-head"><span>VALUES</span><span class="score">1.9</span></header>
      <div class="goal"><p class="goal-text">Inventory Value to be around 1.25 x you last months INVENTORY sales</p><span class="goal-target">1.25</span></div>
      <ol class="rank-list">
        <li class="rank-row is-green"><span class="rank-pos">1</span><span class="store-name">(8) VZaEOSVkef</span><span class="metric">0.2</span></li>
        <li class="rank-row is-green"><span class="rank-pos">2</span><span class="store-name">(3) PcVKNpUNmj</span><span class="metric">0.2</span></li>
        <li class="rank-row is-green"><span class="rank-pos">3</span><span class="store-name">(4) RllyRZsTIn</span><span class="metric">0.4</span></li>
        <li class="rank-row is-green"><span class="rank-pos">4</span><span class="store-name">(9) epiNQFtERO</span><span class="metric">0.6</span></li>
        <li class="rank-row is-green"><span class="rank-pos">5</span><span class="store-name">(3) FbFOzkjSpF</span><span class="metric">0.7</span></li>
        <li class="rank-row is-green"><span class="rank-pos">6</span><span class="store-name">(7) RdzzkcVqtC</span><span class="metric">0.8</span></li>
        <li class="rank-row is-green"><span class="rank-pos">7</span><span class="store-name">(1) DiilXiGkTx</span><span class="metric">0.8</span></li>
        <li class="rank-row is-green"><span class="rank-pos">8</span><span class="store-name">(1) jxWbwORyVa</span><span class="metric">0.8</span></li>
        <li class="rank-row is-green"><span class="rank-pos">9</span><span class="store-name">(4) UyzYfIMzU</span><span class="metric">0.8</span></li>
        <li class="rank-row is-green"><span class="rank-pos">10</span><span class="store-name">&nbsp;(7) SCXulMdjcB</span><span class="metric">1</span></li>
      </ol>
    </section>
  </main>
</body>
</html>
```